OzVoltix and TLW Alert insert/flyer

OzVoltix is an energy consulting firm which has been specializing in energy contract brokering, data management and consulting. We aim to bring value to our customers through open books communication and relevant information relating to their energy consumption. We have created a new patented design for an electricity consumption alert, which we send out monthly to clients. The alert example will be attached below which identifies a change in electricity consumption when compared to the previous month. We would like an advertisement to insert for the release of this insert. We work business to business trying to provide different saving opportunities for each client. We have a slogan currently in place “KEEP YOUR FINGER ON THE PULSE! – Stay aware and save money $$.” We would like to have the attached logos for both companies OzVoltix and TLW, and the contact box included on the insert. Please note, we require these inserts by 13th of november as we have a deadline. Please also find attached the patent number for the alert. Some content we would like to include is below;With the unique and patented energy usage alert system, any consumer connected to the electricity grid in QLD, NSW, ACT, VIC, SA, and TAS with a coms smart meter installed can have access to this system. This system is designed with both residential and commercial deployment in mind. A sample of commercial consumer that will benefit from this alert system but is not limited to:· Large Administrative Centres E.g. Head Office, Call Centres, etc.· Health Facilities – Hospitals – Aged Care Facilities, etc.· Educational Establishments: Universities, Colleges & Schools· Associations for Independent Retailers E.g. Independent supermarkets, Hardware stores· Hotels and Bottle Shops· Various hotel restaurants· Retail stores such as pharmacy store

Target Market(s)

Business in Australia.

Industry/Entity Type

Consulting

Font styles to use
Serif
Sans Serif

Colors

Designer to choose colors to be used in the design.

Requirements
Must have
• Must have OzVoltix and TLW logo, contact box and patent number.
Nice to have
• Alert images and icons, pictures that relate
• Some content we would like to include is below;
• With the unique and patented energy usage alert system, any consumer connected to the electricity grid in QLD, NSW, ACT, VIC, SA, and TAS with a coms smart meter installed can have access to this system. This system is designed with both residential and commercial deployment in mind. A sample of commercial consumer that will benefit from this alert system but is not limited to:
• · Large Administrative Centres E.g. Head Office, Call Centres, etc.
• · Health Facilities – Hospitals – Aged Care Facilities, etc.
• · Educational Establishments: Universities, Colleges & Schools
• · Associations for Independent Retailers E.g. Independent supermarkets, Hardware stores
• · Hotels and Bottle Shops
• · Various hotel restaurants
• · Retail stores such as pharmacy store
Should not have
• Images that have been copied/plagiarized,

```html
<!DOCTYPE html>
<html lang="en">
<head>
<meta charset="utf-8">
<title>OzVoltix – Keep your finger on the pulse</title>
<link rel="stylesheet" href="https://fonts.googleapis.com/css2?family=Open+Sans:wght@400;600;700&family=Arimo:wght@400;700&display=swap">
<style>
  :root {
    --green: #3db54a;
    --green-dark: #2f9a3c;
    --panel: #f3f4f4;
    --bar: #d9dadb;
    --ink: #3a3a3a;
    --ink-soft: #4a4a4a;
    --white: #ffffff;
    --rule: #555555;
    --accent-red: #c8312b;
  }
  * { box-sizing: border-box; margin: 0; padding: 0; }
  html, body { width: 959px; height: 1200px; overflow: hidden; background: var(--white); }
  .flyer { position: relative; width: 959px; height: 1200px; font-family: "Open Sans", sans-serif; color: var(--ink); }

  .hero { position: absolute; left: 0; top: 0; width: 959px; height: 386px; }
  .hero svg { display: block; }
  .brand { position: absolute; left: 40px; top: 62px; display: flex; align-items: center; gap: 10px; }
  .brand-dot { width: 16px; height: 16px; border-radius: 50%; background: var(--white); }
  .brand-name { font-family: "Open Sans", sans-serif; font-weight: 600; font-size: 38px; color: var(--white); letter-spacing: 0.5px; }

  .headline-band { position: absolute; left: 0; top: 386px; width: 959px; height: 122px; background: var(--green); text-align: center; color: var(--white); }
  .headline { font-size: 41px; font-weight: 600; line-height: 1; padding-top: 27px; letter-spacing: 0.2px; }
  .subline { font-size: 20px; font-weight: 700; margin-top: 14px; }
  .pointer { position: absolute; left: 472px; top: 508px; width: 0; height: 0; border-left: 28px solid transparent; border-right: 28px solid transparent; border-top: 22px solid var(--green); z-index: 2; }

  .content { position: absolute; left: 0; top: 508px; width: 959px; height: 392px; background: var(--panel); }
  .alert-sample { position: absolute; left: 0; top: 0; width: 385px; height: 392px; background: var(--white); }
  .alert-sample .sheet { position: absolute; left: 30px; top: 22px; width: 320px; height: 340px; background: linear-gradient(170deg, #f6d53a 0%, #f6d53a 18%, #ececec 30%, #d7d7d7 70%, #6fbf6a 82%, #e5e5e5 92%); transform: rotate(-10deg); border-radius: 2px; }
  .body-copy { position: absolute; left: 478px; top: 56px; width: 524px; font-size: 13.6px; line-height: 15.4px; color: var(--ink-soft); text-align: justify; margin-left: -75px; }
  .benefits { list-style: none; position: absolute; left: 403px; top: 180px; font-size: 14px; line-height: 24.5px; color: var(--ink-soft); }
  .benefits li::before { content: "• "; }
  .benefits .wrap { padding-left: 9px; }
  .partner { position: absolute; left: 808px; top: 276px; display: flex; flex-direction: column; align-items: center; gap: 6px; }
  .partner-square { width: 44px; height: 44px; border: 2px solid var(--accent-red); }
  .partner-name { font-family: "Open Sans", sans-serif; font-size: 11px; font-weight: 400; color: var(--accent-red); white-space: nowrap; }

  .cta-bar { position: absolute; left: 0; top: 900px; width: 959px; height: 55px; background: var(--bar); }
  .cta { position: absolute; left: 24px; top: 6px; width: 902px; height: 44px; border-radius: 14px; background: var(--green); color: var(--white); font-size: 21px; font-weight: 700; text-align: center; line-height: 44px; letter-spacing: 0.6px; box-shadow: 0 2px 0 var(--green-dark); }

  .form { position: absolute; left: 24px; top: 955px; width: 477px; font-family: "Arimo", sans-serif; }
  .field { position: absolute; left: 0; width: 477px; border-bottom: 1.5px solid var(--rule); font-size: 16px; color: var(--ink); padding-left: 0; height: 22px; }
  .contact { position: absolute; left: 546px; top: 962px; width: 380px; font-family: "Arimo", sans-serif; font-size: 16px; color: var(--ink-soft); }
  .contact p { line-height: 28.5px; }
  .contact .lead { margin-bottom: 4px; }
  .contact dl { line-height: 28.5px; }
  .contact dt { display: inline; font-weight: 700; color: #222; }
  .contact dd { display: inline; }
</style>
</head>
<body>
<div class="flyer">

  <header class="hero">
    <svg width="959" height="386" viewBox="0 0 959 386">
      <defs>
        <linearGradient id="skyline" x1="0" y1="0" x2="0" y2="1">
          <stop offset="0" stop-color="#6f8aa3"/>
          <stop offset="0.45" stop-color="#aab8c2"/>
          <stop offset="0.78" stop-color="#e9c27a"/>
          <stop offset="0.9" stop-color="#f2a531"/>
          <stop offset="1" stop-color="#2c2218"/>
        </linearGradient>
      </defs>
      <rect width="959" height="386" fill="var(--green)"/>
      <path d="M0 232 Q 420 82 959 36 L959 50 Q 420 96 0 246 Z" fill="#ffffff"/>
      <path d="M0 246 Q 420 96 959 50 L959 62 Q 420 110 0 258 Z" fill="#c9ccce"/>
      <path d="M0 258 Q 420 110 959 62 L959 386 L0 386 Z" fill="url(#skyline)" role="img" aria-label="Photo of high-voltage transmission towers against a sunset sky"/>
    </svg>
    <div class="brand">
      <span class="brand-dot"></span>
      <span class="brand-name">OzVoltix</span>
    </div>
  </header>

  <section class="headline-band">
    <h1 class="headline">KEEP YOUR FINGER ON THE PULSE!</h1>
    <p class="subline">Stay aware and save money $$</p>
  </section>
  <div class="pointer"></div>

  <section class="content">
    <div class="alert-sample">
      <div class="sheet" role="img" aria-label="Sample TLW Alert electricity alert sheet showing monthly consumption comparison"></div>
    </div>
    <p class="body-copy">With the unique and patented energy usage alert system, any consumer connected to the electricity grid in QLD, NSW, ACT, VIC, SA, and TAS with a coms smart meter installed can have access to this system. This system is designed with both residential and commercial deployment in mind. A sample of commercial consumer that will benefit from this alert system but is not limited to:</p>
    <ul class="benefits">
      <li>Large Administrative Centres E.g. Head Office, Call Centres, etc.</li>
      <li>Health Facilities – Hospitals – Aged Care Facilities, etc.</li>
      <li>Educational Establishments: Universities, Colleges &amp; Schools</li>
      <li>Associations for Independent Retailers E.g. Independent supermarkets,<br><span class="wrap">Hardware stores</span></li>
      <li>Hotels and Bottle Shops</li>
      <li>Various hotel restaurants</li>
      <li>Retail stores such as pharmacy store</li>
    </ul>
    <div class="partner">
      <span class="partner-square"></span>
      <span class="partner-name">TLW Metering Data</span>
    </div>
  </section>

  <div class="cta-bar">
    <div class="cta">Get your complimentary electicity review today!</div>
  </div>

  <form class="form">
    <div class="field" style="top:27px">Name:</div>
    <div class="field" style="top:67px">Email:</div>
    <div class="field" style="top:108px">Phone:</div>
    <div class="field" style="top:149px">Address:</div>
    <div class="field" style="top:188px"></div>
  </form>

  <aside class="contact">
    <p class="lead">SMS, fax or email this completed form along with a recent energy bill, and we’ll get back to you ASAP!</p>
    <dl>
      <div><dt>SMS:</dt> <dd>0400 555 318</dd></div>
      <div><dt>Phone:</dt> <dd>1300 555 207</dd> <dt>Fax:</dt> <dd>(03) 9555 0142</dd></div>
      <div><dt>Email:</dt> <dd>hello@ozvoltix.com</dd></div>
      <div><dt>Web:</dt> <dd>www.ozvoltix.com</dd></div>
    </dl>
  </aside>

</div>
</body>
</html>
```